Hardcore nerd needs to stand out in a sea of dull Defence business cards

Wombeck Dynamics is a new Australian consulting engineering company that turns research and theory into practical systems. No evangelistic fluff, just mathematics and physics into electronic and optical circuits for consumer products, scientific research or Defence applications.

We already have a recognised logo (provided) which is often dark blue/black on a light background but we're open to other combinations. (Us engineers tend to have limited aesthetic imagination :)

Some of our recent products have included:
* Instrumentation for electrical testing,
* Radar jammers,
* GPS antenna design,
* Satellite tracking systems,
* High power lasers

We're open to both single and double-sided designs - happy to be convinced either way.

P.S. Another group is working on the web page, so - alas - our web site is currently of no use for images/ideas...

Target Market(s)

Engineering managers,
Scientists

Contact Information for Business Card

Dr Martin Folsey
R&D Engineer

martin@wombeckdynamics.com.au
0427 563 201

PO Box XXX (to be confirmed)
Brindlow ACT 2914
Australia

Font styles to use
Serif
Sans Serif

Colors

Designer to choose colors to be used in the design.

Requirements
Must have
• My contact details!
• I've had many (great) "bold and plain" designs submitted already, so feel free to be artistically creative :)
• Happy to take advice re fonts/colours/printability etc.
Nice to have
• I'm not sure if "lists" are more at home on a CV than a business card, but representative services include:
• Applied electromagnetics
• RF and high speed electronics
• Signal and image processing
• Electro-optical and laser systems
• Concept-to-prototype design services
• If you're considering double sided cards, then often measuring/alignment grids/rulers feature on the back of similar cards.
• e.g. https://www.kelvorin.com/newgrouppage9.cfm?objectgroup_id=4183
• https://www.kelvorin.com/newgrouppage9.cfm?objectgroup_ID=4185
• ..or even a "Smith chart" (google will return lots)
• Generic images to represent a capability might work - googling images associated with keyword for each of these areas might help:
• - "passive radar", "phased array", "fdtd", "vircator"
• RF and high speed electronic design
• - "smith chart", "microstrip circuits", "dimensioned drawing", "electronic schematic"
• - "dft", "iir filter"
• - "optical cavity". "laser energy level diagram"
• Background/watermarked images outlines/wireframes/schematics would probably look OK.
Should not have
• If a list of projects/services is provided, it is important not to make the client feel that this is "all" the company can do. Engineering design is a creative discipline (like graphics :)
• Please, no stock "military" snaps like planes, missiles, etc!

```html
<!DOCTYPE html>
<html lang="en">
<head>
<meta charset="utf-8">
<title>Wombeck Dynamics – Business Card</title>
<link rel="stylesheet" href="https://fonts.googleapis.com/css2?family=Open+Sans:ital,wght@0,400;0,700;1,400&display=swap">
<style>
  :root {
    --navy: #1f2a66;
    --navy-deep: #1b2458;
    --navy-light: #34468f;
    --orange: #f47f20;
    --orange-light: #f9a833;
    --white: #ffffff;
    --stage: #e9e9ec;
  }
  * { box-sizing: border-box; margin: 0; padding: 0; }
  html, body {
    width: 1200px; height: 900px; overflow: hidden;
    background: var(--stage);
    font-family: "Open Sans", Arial, sans-serif;
  }
  .stage {
    position: relative; width: 1200px; height: 900px;
  }
  .card {
    position: absolute;
    width: 620px; height: 354px;
    border-radius: 22px;
    overflow: hidden;
    box-shadow: 0 10px 28px rgba(0,0,0,0.22);
  }
  /* back side */
  .card-back {
    left: 470px; top: 60px;
    background: linear-gradient(135deg, var(--navy-deep) 0%, var(--navy) 45%, var(--navy-light) 100%);
  }
  .back-brand {
    position: absolute; left: 150px; top: 132px;
    display: flex; align-items: center; gap: 18px;
  }
  .brand-dot {
    width: 70px; height: 70px; border-radius: 50%;
    background: var(--white);
  }
  .brand-name {
    font-weight: 700; color: var(--white);
    font-size: 30px; line-height: 1.05; letter-spacing: 1px;
    text-transform: uppercase;
  }
  /* front side */
  .card-front {
    left: 110px; top: 480px;
    background: var(--white);
  }
  .front-art { position: absolute; inset: 0; width: 100%; height: 100%; }
  .contact {
    position: absolute; left: 38px; top: 78px;
    color: var(--white);
    font-size: 15px; line-height: 23px;
  }
  .contact .name { font-weight: 700; font-size: 23px; line-height: 30px; }
  .contact .role { font-style: italic; }
  .contact .line { display: flex; align-items: center; gap: 7px; }
  .contact .icon { width: 15px; height: 15px; flex: none; }
  .front-brand {
    position: absolute; right: 34px; top: 92px;
    display: flex; align-items: center; gap: 14px;
  }
  .front-brand .brand-dot { width: 58px; height: 58px; background: var(--navy); }
  .front-brand .brand-name { color: var(--navy); font-size: 26px; }
</style>
</head>
<body>
<main class="stage">

  <section class="card card-back" aria-label="Card back">
    <div class="back-brand">
      <span class="brand-dot"></span>
      <span class="brand-name">Wombeck<br>Dynamics</span>
    </div>
  </section>

  <section class="card card-front" aria-label="Card front">
    <svg class="front-art" viewBox="0 0 620 354" preserveAspectRatio="none" aria-hidden="true">
      <defs>
        <linearGradient id="orangeFill" x1="0.3" y1="0" x2="0.6" y2="1">
          <stop offset="0" stop-color="var(--orange-light)"/>
          <stop offset="0.55" stop-color="var(--orange)"/>
          <stop offset="1" stop-color="var(--orange)"/>
        </linearGradient>
      </defs>
      <path d="M0,40 C160,34 270,62 340,145 C400,220 430,290 620,292 L620,354 L0,354 Z" fill="var(--navy)"/>
      <path d="M0,50 C155,46 262,76 330,155 C392,232 424,312 620,314 L620,354 L0,354 Z" fill="var(--white)"/>
      <path d="M0,54 C152,50 258,80 326,160 C388,238 420,320 620,322 L620,354 L0,354 Z" fill="url(#orangeFill)"/>
    </svg>

    <div class="contact">
      <p class="name">Dr Martin Folsey</p>
      <p class="role">R&amp;D Engineer</p>
      <p>PO Box XXX</p>
      <p>Brindlow ACT 2914, Australia</p>
      <p class="line">
        <svg class="icon" viewBox="0 0 16 16" aria-hidden="true"><circle cx="8" cy="8" r="7" fill="none" stroke="#fff" stroke-width="1.4"/><path d="M5 5.2c0 3 2.8 5.8 5.8 5.8l.9-1.3-1.6-1-0.8.7c-1-.4-2-1.4-2.4-2.4l.7-.8-1-1.6z" fill="#fff"/></svg>
        <span>0427 563 201</span>
      </p>
      <p class="line">
        <svg class="icon" viewBox="0 0 16 16" aria-hidden="true"><circle cx="8" cy="8" r="7" fill="none" stroke="#fff" stroke-width="1.4"/><rect x="4.3" y="5.3" width="7.4" height="5.4" fill="none" stroke="#fff" stroke-width="1.1"/><path d="M4.3 5.3 8 8.3l3.7-3" fill="none" stroke="#fff" stroke-width="1.1"/></svg>
        <span>martin@wombeckdynamics.com.au</span>
      </p>
    </div>

    <div class="front-brand">
      <span class="brand-dot"></span>
      <span class="brand-name">Wombeck<br>Dynamics</span>
    </div>
  </section>

</main>
</body>
</html>
```